Graphic Design Illustrating Women's Suffrage by Country Over Time

This project includes a total of 10 designs. Nine of them are to be n the form of "puzzle pieces" that, when fit together, create the head of a woman looking optimistically and determinedly up toward the future. These puzzle pieces are formed primarily of the names of countries, in the order in which they granted women's suffrage. These puzzle pieces are also to include non-word elements to help form the shape, look and feel of the woman's head, neck and possibly shoulders, as well as the sense of a rising sun behind her. Files have been included that provide you with the nine lists (in order), which show an example master design (that has a lot of errors in it, so read all the information included in this brief to know both what to do and what NOT to do), and also which should examples of the puzzle pieces (these pieces also have errors, so again read everything carefully).

Target Market(s)

This isn't the "target market" informational here, but rather where and how this image will be used. This set of 10 images (9 word clouds forming one master design when put together) will help tell the story of the birth of women's suffrage throughout the world. The "master design" of the woman's head, along with each of the individual designs, will ultimately be placed on pages of a 6 inch by 9 inch book printed on a light ivory paper in greyscale. It will also be published separately online, but the primary use is within the book. **The white space available to print each of the 10 designs is a maximum size of 4.5 inches by 6.75 inches.**

Industry/Entity Type

Book Publisher

Font styles to use
Serif
Sans Serif
Decorative
Script

Colors

Designer to choose only greyscale colors for use in the design.

Requirements
Must have
• The woman's race must not be recognizable. The puzzle pieces are made up of sets of country names. These are the countries that have granted women the right to vote--which now include all countries on Earth save the Holy See/Vatican City. The "sets of countries" are lists of these countries separated in time by the date in which they granted women the right to vote. The lists are mostly divided by decade, but that isn't relevant for you, all you need to know is that there are nine sequential lists. [List Placement into the Master Design] The first list wants to form the puzzle piece that is at the very bottom and/or bottom right of the design. The second list will then be placed either to the left of that bottom right piece, and/or above a bottom piece and to the left. The third list could be to the right of the second and/or above the first or second. It is okay to vary right or left placement. It is okay to put one, two or even three lists on on the same "level" as any other list that precedes it. But on the whole the design must be "built," like a building is built, from the bottom us. Thus, the first pieces form a foundation upon which later pieces are then placed. There should never be a puzzle piece that is "hanging" with white space below it, within the master design. Within he book's pages, slowly the pieces will be added together to form the master design. By the time the eighth puzzle piece is added, the entire head and neck (perhaps shoulders too) of the woman has appeared--indicating visually to the reader that the fight for worldwide women's suffrage was nearly done! But not quite. Only eleven or so countries remained as holdouts, at that point. To represent the addition of these eleven countries (in List 9), these country names will form a semi-circle around the woman's face, thus "illuminating" the woman's head by creating the edge of a rising sun. An example of the master design, as well as how the country lists could be put together, are provided in the files, [MUST HAVES and WHAT TO WATCH FOR] HOWEVER, that designer placed the lists a) in the wrong order of the design (so do NOT simply repeat what they did!). That designer also used b) all caps and c) the same font, as well as d) putting everything in all black and using white only as a design element (not using it for forming any of the country names). Also, e) the prior designer's puzzle pieces were only the words of the country names themselves. In the winning design, each puzzle piece must include ALL design elements (for that 'piece', i.e., the country names as well as non-word design elements). Thus when placed together the nine designs create the entire "finished puzzle." Finally, in the individual puzzle pieces f) some of the country names were so small they were unreadable (unless you have excellent vision) when the piece is placed by itself onto a 4.5 inch by 6.75 inch white page, and that is unacceptable. CRITICAL: The winner of this contest must show ALL 10 designs in their final submitted entry in order to win. IMPORTANT: While the country names may be somewhat difficult to read when seen in the overall master design, it is vital that the country names be readable in each of the individual 9 puzzle pieces. Also critical: Within each puzzle piece, country names want to be placed into the design in the order they are found on the lists. If and only if you find it necessary, a VERY few exceptions might be made to this "countries in the order they appear on each list" rule, for the sake of the look and feel of the design.
Nice to have
• In order to create the overall design, you will probably need to use elements that are not part of the liist of countries (see example in files). That is fine. The best designs will find a way to create greater depth in the design through the use of 25-40+ or so different fonts, so that no country next to another uses the same font. It will not make use of all caps for every country (though all caps is ok to use in many cases). It will make use of greyscale, so that every country is in a different tone of grey, some light, some dark, some all black. The size of the the country names can also vary. Even individual letters within words can vary in size, so long as the entire word is readable when he puzzle piece is placed into the 4.5 inch by 6.75 inch white space on which it will be displayed in the book. It would also be fine to use white or light grey words inside black or dark grey backgrounds, where those backgrounds then help form parts of the head of the woman or her hair or facial features, etc. The example design does not do this. It only uses solid black backgrounds to form the head, locks of hair and facial features of the woman. You could possibly be more creative with the use of black background by incorporating some of the country names into these solid black locations, so long as doing so works for the overall look and feel of the master design.
Should not have
• Only using all caps, only using all the same font, or only using all black and no greys. Should not mixi the order in which country names appear (except perhaps once or twice max. Ideally, never--but you may have to for the look and feel of your design). Placing puzzle pieces into the master design that---when so placed, in order--have a puzzle piece "hanging" over white space, waiting for the addition of another piece (see Must Haves above); these puzzle pieces are SEQUENTIAL and are to build the master design one at a time from the bottom up (though it's okay to build parts of the left side up of the design up before parts of the right, or vice versa--just no pieces hanging over white space). No clear "race" should be determinable by the master design of the woman's head--she is to represent every woman on Earth. Ask me questions if you have them!

```html
<!DOCTYPE html>
<html lang="en">
<head>
<meta charset="utf-8">
<title>Rising Sun Arc — List Nine</title>
<link rel="stylesheet" href="https://fonts.googleapis.com/css2?family=Tinos&family=Rokkitt:wght@300&family=Fjalla+One&family=Libre+Baskerville&family=Quicksand:wght@400&family=Gilda+Display&family=Kalam:wght@300&family=Archivo:wght@700&family=Arimo&family=Lato:wght@300&display=swap">
<style>
  :root {
    --paper: #ffffff;
    --ink-black: #000000;
    --ink-charcoal: #2b2b2b;
    --ink-dark: #3c3c3c;
    --ink-mid: #555555;
    --ink-soft: #6e6e6e;
    --ink-light: #7a7a7a;
  }
  html, body {
    margin: 0;
    padding: 0;
    width: 1200px;
    height: 1200px;
    overflow: hidden;
    background: var(--paper);
  }
  .sun-arc { display: block; width: 1200px; height: 1200px; }
  .liechtenstein { font-family: "Tinos", serif; font-size: 29px; fill: var(--ink-black); }
  .kuwait { font-family: "Rokkitt", serif; font-weight: 300; font-size: 48px; fill: var(--ink-mid); letter-spacing: 1px; }
  .central-african-republic { font-family: "Fjalla One", sans-serif; font-size: 30px; fill: var(--ink-dark); }
  .namibia { font-family: "Libre Baskerville", serif; font-size: 35px; fill: var(--ink-black); }
  .samoa { font-family: "Quicksand", sans-serif; font-size: 33px; fill: var(--ink-light); }
  .qatar { font-family: "Gilda Display", serif; font-size: 38px; fill: var(--ink-black); }
  .bahrain { font-family: "Kalam", cursive; font-weight: 300; font-size: 33px; fill: var(--ink-light); }
  .oman { font-family: "Archivo", sans-serif; font-weight: 700; font-size: 37px; fill: var(--ink-mid); }
  .uae { font-family: "Arimo", sans-serif; font-size: 28px; fill: var(--ink-charcoal); }
  .saudi-arabia { font-family: "Lato", sans-serif; font-weight: 300; font-size: 38px; fill: var(--ink-dark); }
</style>
</head>
<body>
<svg class="sun-arc" viewBox="0 0 1200 1200" xmlns="http://www.w3.org/2000/svg" role="img" aria-label="List nine country names forming the edge of a rising sun">
  <defs>
    <path id="sun-edge" d="M 158 927 A 530 530 0 1 1 1108 831" fill="none"/>
  </defs>
  <text class="liechtenstein"><textPath href="#sun-edge" startOffset="0">Liechtenstein</textPath></text>
  <text class="kuwait"><textPath href="#sun-edge" startOffset="208">Kuwait</textPath></text>
  <text class="central-african-republic"><textPath href="#sun-edge" startOffset="375">Central African Republic</textPath></text>
  <text class="namibia"><textPath href="#sun-edge" startOffset="683">Namibia</textPath></text>
  <text class="samoa"><textPath href="#sun-edge" startOffset="845">Samoa</textPath></text>
  <text class="qatar"><textPath href="#sun-edge" startOffset="964">Qatar</textPath></text>
  <text class="bahrain"><textPath href="#sun-edge" startOffset="1072">Bahrain</textPath></text>
  <text class="oman"><textPath href="#sun-edge" startOffset="1202">Oman</textPath></text>
  <text class="uae"><textPath href="#sun-edge" startOffset="1313">United Arab Emirates</textPath></text>
  <text class="saudi-arabia"><textPath href="#sun-edge" startOffset="1620">Saudi Arabia</textPath></text>
</svg>
</body>
</html>
```